Dell Brunow for Columbia County Commissioner

3"x12" sized bumper sticker design based on the provided logo.

Please also include Vote November 4 or just November 4 somewhere in the design.

```html
<!DOCTYPE html>
<html lang="en">
<head>
<meta charset="utf-8">
<title>Dell Brunow for Columbia County Commissioner – Bumper Sticker</title>
<link rel="stylesheet" href="https://fonts.googleapis.com/css2?family=Cinzel:wght@400;500&display=swap">
<style>
  :root {
    --navy: #1a2642;
    --red: #c01f32;
    --white: #ffffff;
    --page: #ffffff;
  }
  html, body {
    margin: 0;
    padding: 0;
    width: 1200px;
    height: 1100px;
    overflow: hidden;
    background: var(--page);
  }
  .canvas {
    position: relative;
    width: 1200px;
    height: 1100px;
  }
  .sticker {
    position: absolute;
    left: 20px;
    top: 405px;
    width: 1158px;
    height: 288px;
    background: var(--navy);
    font-family: "Cinzel", "Trajan Pro", serif;
    color: var(--white);
  }
  .stripes {
    position: absolute;
    left: 0;
    top: 0;
    width: 1158px;
    height: 288px;
  }
  .candidate-name {
    position: absolute;
    left: 40px;
    top: 0px;
    margin: 0;
    font-size: 108px;
    font-weight: 400;
    line-height: 1;
    letter-spacing: 1px;
    white-space: nowrap;
  }
  .office {
    position: absolute;
    right: 28px;
    top: 104px;
    margin: 0;
    white-space: nowrap;
    line-height: 1;
    font-weight: 400;
  }
  .office .county {
    font-size: 42px;
    letter-spacing: 1px;
    margin-right: 10px;
  }
  .office .title {
    font-size: 66px;
    letter-spacing: 1px;
  }
  .election {
    position: absolute;
    left: 798px;
    width: 262px;
    top: 178px;
    text-align: center;
    line-height: 1;
  }
  .election .vote {
    display: block;
    font-size: 54px;
    font-weight: 500;
    letter-spacing: 1px;
  }
  .election .date {
    display: block;
    margin-top: 4px;
    font-size: 31px;
    font-weight: 500;
    letter-spacing: 1px;
  }
</style>
</head>
<body>
<div class="canvas">
  <section class="sticker" aria-label="Dell Brunow for Columbia County Commissioner bumper sticker">
    <svg class="stripes" viewBox="0 0 1158 288" aria-hidden="true">
      <rect x="0" y="188" width="798" height="20" fill="var(--red)"/>
      <rect x="0" y="216" width="798" height="19" fill="var(--white)"/>
      <rect x="0" y="243" width="798" height="20" fill="var(--red)"/>
      <rect x="1060" y="188" width="98" height="20" fill="var(--red)"/>
      <rect x="1060" y="216" width="98" height="19" fill="var(--white)"/>
      <rect x="1060" y="243" width="98" height="20" fill="var(--red)"/>
    </svg>
    <h1 class="candidate-name">Dell Brunow</h1>
    <p class="office"><span class="county">columbia county</span><span class="title">COMMISSIONER</span></p>
    <p class="election"><span class="vote">Vote</span><span class="date">November 4</span></p>
  </section>
</div>
</body>
</html>
```